New Business Card Design Project

We are a spa looking to create a professional elegant business card for a spa mainly black and white with a splash of lime green. This card will be two sided - the front side will have an image, the logo, and the spa's information - the back side will have a promotion for new customers - NEW CUSTOMERS $20 OFF

Look and feel: chic, modern, and spa-ish.
Information to be included:
Therapist Name
Therapist specialty
Address: 5147 Marlowe Ave, Beverly Hills CA 90211
Phone: (310) 482-3961

Let me know if you have any questions!

Thank you

```html
<!DOCTYPE html>
<html lang="en">
<head>
<meta charset="utf-8">
<title>Larkin Day Spa – Business Card</title>
<link rel="stylesheet" href="https://fonts.googleapis.com/css2?family=Raleway:wght@500;600&family=Great+Vibes&family=Cinzel:wght@600&display=swap">
<style>
  :root {
    --backdrop: #e4e0dc;
    --card-black: #121212;
    --card-charcoal: #2a2a2a;
    --paper-white: #f4f4f2;
    --soft-white: #dcdcdc;
    --lime: #8cc63f;
    --card-w: 520px;
    --card-h: 300px;
  }
  * { box-sizing: border-box; margin: 0; padding: 0; }
  html, body {
    width: 1200px;
    height: 800px;
    overflow: hidden;
    background: var(--backdrop);
  }
  .canvas {
    width: 1200px;
    height: 800px;
    display: flex;
    align-items: center;
    justify-content: center;
    gap: 48px;
  }
  .card {
    position: relative;
    width: var(--card-w);
    height: var(--card-h);
    background: var(--card-black);
    border-radius: 4px;
    overflow: hidden;
    box-shadow: 0 10px 24px rgba(0, 0, 0, 0.22);
    color: var(--paper-white);
    font-family: "Raleway", sans-serif;
  }
  .card__pattern {
    position: absolute;
    inset: 0;
    background:
      radial-gradient(ellipse at 25% 35%, var(--card-charcoal) 0%, transparent 55%),
      radial-gradient(ellipse at 70% 70%, #232323 0%, transparent 50%),
      radial-gradient(ellipse at 85% 20%, #1e1e1e 0%, transparent 40%),
      var(--card-black);
  }
  .brand {
    position: absolute;
    display: flex;
    align-items: center;
    gap: 12px;
  }
  .brand__dot {
    width: 14px;
    height: 14px;
    border-radius: 50%;
    background: var(--lime);
  }
  .brand__name {
    font-family: "Raleway", sans-serif;
    font-weight: 600;
    font-size: 24px;
    letter-spacing: 3px;
    text-transform: uppercase;
    color: var(--paper-white);
  }

  /* Front */
  .card--front .brand { left: 36px; top: 42px; }
  .therapist {
    position: absolute;
    left: 250px;
    top: 112px;
  }
  .therapist__name {
    font-family: "Great Vibes", cursive;
    font-size: 44px;
    line-height: 1;
    color: var(--paper-white);
  }
  .therapist__role {
    font-size: 24px;
    font-weight: 500;
    color: var(--lime);
    margin: 2px 0 0 40px;
  }
  .contact {
    position: absolute;
    left: 36px;
    right: 36px;
    bottom: 34px;
    list-style: none;
    font-size: 17px;
    font-weight: 600;
    color: var(--soft-white);
  }
  .contact__item {
    display: flex;
    align-items: center;
    gap: 8px;
    margin-top: 10px;
  }
  .contact__item--phone { justify-content: flex-end; }
  .contact__icon { width: 18px; height: 18px; fill: var(--lime); flex: none; }

  /* Back */
  .card--back .brand {
    left: 50%;
    top: 48px;
    transform: translateX(-50%);
  }
  .promo {
    position: absolute;
    left: 0;
    right: 0;
    bottom: 54px;
    text-align: center;
  }
  .promo__label {
    font-family: "Raleway", sans-serif;
    font-weight: 600;
    font-size: 20px;
    letter-spacing: 5px;
    color: var(--soft-white);
    margin-bottom: 6px;
  }
  .promo__offer {
    font-family: "Cinzel", serif;
    font-weight: 600;
    font-size: 52px;
    line-height: 1.1;
    letter-spacing: 2px;
  }
  .promo__amount { color: var(--lime); }
  .promo__word { color: var(--paper-white); }
</style>
</head>
<body>
<main class="canvas">

  <section class="card card--front" aria-label="Business card front">
    <div class="card__pattern" role="img" aria-label="Dark charcoal paisley pattern image filling the card"></div>
    <div class="brand">
      <span class="brand__dot"></span>
      <span class="brand__name">Larkin Day Spa</span>
    </div>
    <div class="therapist">
      <p class="therapist__name">Evan Reyes</p>
      <p class="therapist__role">therapist</p>
    </div>
    <ul class="contact">
      <li class="contact__item">
        <svg class="contact__icon" viewBox="0 0 16 16" aria-hidden="true"><path d="M8 1 L15 7.5 H13 V15 H9.5 V10.5 H6.5 V15 H3 V7.5 H1 Z"/></svg>
        5147 Marlowe Ave, Beverly Hills CA 90211
      </li>
      <li class="contact__item contact__item--phone">
        <svg class="contact__icon" viewBox="0 0 16 16" aria-hidden="true"><path d="M4.2 1.5 L6.3 4.6 L5 6.2 C5.8 8 7.9 10.2 9.8 11 L11.4 9.7 L14.5 11.8 L13.2 14.2 C8 14 2 8 1.8 2.8 Z"/></svg>
        (310) 482-3961
      </li>
    </ul>
  </section>

  <section class="card card--back" aria-label="Business card back">
    <div class="card__pattern" role="img" aria-label="Dark charcoal paisley pattern image filling the card"></div>
    <div class="brand">
      <span class="brand__dot"></span>
      <span class="brand__name">Larkin Day Spa</span>
    </div>
    <div class="promo">
      <p class="promo__label">NEW CUSTOMERS</p>
      <p class="promo__offer"><span class="promo__amount">$20</span> <span class="promo__word">OFF</span></p>
    </div>
  </section>

</main>
</body>
</html>
```